New Attorney in Non-Traditional Field Needs Creative Edgy Legal Business Card with Side Business Not

I need a new personal business card. Away from the silver lettering on heavy white card stock, Velvet Harbor anyone? I'm newly admitted to the CA bar, I started my own small side-business in sales, I'm arbitrating on a part time basis, and I'm creating a ViewCast channel about current news from young professionals' perspective in January. On the side I've been taking a lot of home buying negotiation classes, and I do a lot of yoga. It would be my dream job to advise clients in the startup/entrepreneurial world. I would like my Viewcast channel, website (www.marlowbead.example/ninaprell), phone number, email, admittance #, and link for workweb featured on my card. The colors and message of homepage www.calmheronflow.example really speak to me. Often I'll read that Mavis Token quote about doing one thing for your brand everyday, and I believe it in wholeheartedly.
Updates

Perrin's design has been accepted with very minimal changes. Thank you all for your submissions. This has been a fun experience.

Target Market(s)

all young attorneys, small startups, small tech, potential employers, networking events for lawyers and other young professionals

Industry/Entity Type

Business

Contact Information for Business Card

Rosalind K. Prell, Esq.
Attorney bar card number
Ph (555) 482-7716
Email Nina.Prell@mailbox.example
Work web website
Viewcast Channel coming soon!
Marlow & Bead website

Font styles to use
Sans Serif
Decorative

Requirements
Must have
• A simple image or logo that can transition to other products as I build my brand. Great colors. Maybe all white & gold? Maybe a cool blues/purples motif?

```html
<!DOCTYPE html>
<html lang="en">
<head>
<meta charset="utf-8">
<title>Rosalind K. Prell – Business Card Options</title>
<link href="https://fonts.googleapis.com/css2?family=Questrial&family=Satisfy&family=Abel&display=swap" rel="stylesheet">
<style>
  :root {
    --canvas: #ffffff;
    --label: #b9b9b6;
    --contact-text: #ffffff;
  }
  * { box-sizing: border-box; margin: 0; padding: 0; }
  html, body { width: 1200px; height: 1000px; overflow: hidden; background: var(--canvas); }
  .sheet { position: relative; width: 1200px; height: 1000px; }

  .option {
    position: absolute; left: 240px; width: 860px; height: 196px;
  }
  .option--01 { top: 48px;
    --front-bg: #e9e4bd; --mark: #ec5a48; --name: #1e1e1e; --title: #e8604d;
    --back-bg: #ec5a48; --icon-bg: #1c1c1c; --icon-fg: #ffffff; --rule: #f6d6c8; }
  .option--02 { top: 286px;
    --front-bg: #a6a89a; --mark: #f6c2b8; --name: #f6c2b8; --title: #ffffff;
    --back-bg: #a6a89a; --icon-bg: #f4ebe6; --icon-fg: #f1a79b; --rule: #e4e2da; }
  .option--03 { top: 523px;
    --front-bg: #e2d5b5; --mark: #e0646f; --name: #6e5a6a; --title: #d75a6a;
    --back-bg: #ea7479; --icon-bg: #7a6070; --icon-fg: #ffffff; --rule: #f6d9c6; }
  .option--04 { top: 761px;
    --front-bg: #f7f1e0; --mark: #c8cd98; --name: #5b4a3f; --title: #c6c38c;
    --back-bg: #836650; --icon-bg: #f7f1e0; --icon-fg: #836650; --rule: #d8cab8; }

  .card { position: absolute; top: 0; width: 343px; height: 196px; overflow: hidden; }
  .card--front { left: 0; background: var(--front-bg); }
  .card--back { left: 377px; background: var(--back-bg); }

  .brand-square {
    position: absolute; left: 48px; top: 63px; width: 70px; height: 70px;
    background: var(--mark);
  }
  .holder-name {
    position: absolute; left: 137px; top: 87px;
    font-family: "Questrial", sans-serif; font-size: 17px; color: var(--name);
    white-space: nowrap;
  }
  .holder-title {
    position: absolute; left: 137px; top: 108px;
    font-family: "Satisfy", cursive; font-size: 15px; color: var(--title);
    white-space: nowrap;
  }

  .contact-list { position: absolute; right: 70px; list-style: none; }
  .contact-list--direct { top: 35px; }
  .contact-list--social { top: 108px; }
  .contact-list li {
    position: relative; height: 18.5px; line-height: 14px;
    font-family: "Questrial", sans-serif; font-size: 10.5px;
    color: var(--contact-text); text-align: right; white-space: nowrap;
  }
  .contact-icon {
    position: absolute; right: -32px; top: 0; width: 14px; height: 14px;
  }
  .contact-icon circle.disc { fill: var(--icon-bg); }
  .contact-icon .glyph { stroke: var(--icon-fg); fill: none; stroke-width: 1.1; }
  .contact-icon .glyph-fill { fill: var(--icon-fg); }
  .contact-rule {
    position: absolute; left: 77px; top: 97px; width: 157px; height: 1px;
    background: var(--rule);
  }

  .option-label {
    position: absolute; left: 737px; top: 174px;
    font-family: "Abel", sans-serif; font-size: 24px; letter-spacing: 0.5px;
    color: var(--label); line-height: 24px; white-space: nowrap;
  }
</style>
</head>
<body>
<main class="sheet">

  <!-- reusable icon markup repeated per option -->
  <section class="option option--01">
    <div class="card card--front">
      <div class="brand-square"></div>
      <p class="holder-name">Rosalind K. Prell</p>
      <p class="holder-title">Esq. Attorney Bar</p>
    </div>
    <div class="card card--back">
      <ul class="contact-list contact-list--direct">
        <li>(555) 482-7716<svg class="contact-icon" viewBox="0 0 14 14"><circle class="disc" cx="7" cy="7" r="7"/><path class="glyph-fill" d="M4.5 3.6l1.3-.3.8 1.8-.9.7c.4.9 1.1 1.6 2 2l.7-.9 1.8.8-.3 1.3c-2.9.2-5.6-2.5-5.4-5.4z"/></svg></li>
        <li>Nina.Prell@mailbox.example<svg class="contact-icon" viewBox="0 0 14 14"><circle class="disc" cx="7" cy="7" r="7"/><rect class="glyph" x="3.8" y="4.8" width="6.4" height="4.4"/><path class="glyph" d="M3.8 4.8L7 7.4l3.2-2.6"/></svg></li>
        <li>www.marlowbead.example/ninaprell<svg class="contact-icon" viewBox="0 0 14 14"><circle class="disc" cx="7" cy="7" r="7"/><circle class="glyph" cx="7" cy="7" r="3.4"/><path class="glyph" d="M3.6 7h6.8M7 3.6c-1.6 2-1.6 4.8 0 6.8M7 3.6c1.6 2 1.6 4.8 0 6.8"/></svg></li>
      </ul>
      <div class="contact-rule"></div>
      <ul class="contact-list contact-list--social">
        <li>Viewcastlinkcontent<svg class="contact-icon" viewBox="0 0 14 14"><circle class="disc" cx="7" cy="7" r="7"/></svg></li>
        <li>Flitterlinkcontent<svg class="contact-icon" viewBox="0 0 14 14"><circle class="disc" cx="7" cy="7" r="7"/></svg></li>
        <li>workweblinkcontent<svg class="contact-icon" viewBox="0 0 14 14"><circle class="disc" cx="7" cy="7" r="7"/></svg></li>
      </ul>
    </div>
    <p class="option-label">OPTION 01</p>
  </section>

  <section class="option option--02">
    <div class="card card--front">
      <div class="brand-square"></div>
      <p class="holder-name">Rosalind K. Prell</p>
      <p class="holder-title">Esq. Attorney Bar</p>
    </div>
    <div class="card card--back">
      <ul class="contact-list contact-list--direct">
        <li>(555) 482-7716<svg class="contact-icon" viewBox="0 0 14 14"><circle class="disc" cx="7" cy="7" r="7"/><path class="glyph-fill" d="M4.5 3.6l1.3-.3.8 1.8-.9.7c.4.9 1.1 1.6 2 2l.7-.9 1.8.8-.3 1.3c-2.9.2-5.6-2.5-5.4-5.4z"/></svg></li>
        <li>Nina.Prell@mailbox.example<svg class="contact-icon" viewBox="0 0 14 14"><circle class="disc" cx="7" cy="7" r="7"/><rect class="glyph" x="3.8" y="4.8" width="6.4" height="4.4"/><path class="glyph" d="M3.8 4.8L7 7.4l3.2-2.6"/></svg></li>
        <li>www.marlowbead.example/ninaprell<svg class="contact-icon" viewBox="0 0 14 14"><circle class="disc" cx="7" cy="7" r="7"/><circle class="glyph" cx="7" cy="7" r="3.4"/><path class="glyph" d="M3.6 7h6.8M7 3.6c-1.6 2-1.6 4.8 0 6.8M7 3.6c1.6 2 1.6 4.8 0 6.8"/></svg></li>
      </ul>
      <div class="contact-rule"></div>
      <ul class="contact-list contact-list--social">
        <li>Viewcastlinkcontent<svg class="contact-icon" viewBox="0 0 14 14"><circle class="disc" cx="7" cy="7" r="7"/></svg></li>
        <li>Flitterlinkcontent<svg class="contact-icon" viewBox="0 0 14 14"><circle class="disc" cx="7" cy="7" r="7"/></svg></li>
        <li>workweblinkcontent<svg class="contact-icon" viewBox="0 0 14 14"><circle class="disc" cx="7" cy="7" r="7"/></svg></li>
      </ul>
    </div>
    <p class="option-label">OPTION 02</p>
  </section>

  <section class="option option--03">
    <div class="card card--front">
      <div class="brand-square"></div>
      <p class="holder-name">Rosalind K. Prell</p>
      <p class="holder-title">Esq. Attorney Bar</p>
    </div>
    <div class="card card--back">
      <ul class="contact-list contact-list--direct">
        <li>(555) 482-7716<svg class="contact-icon" viewBox="0 0 14 14"><circle class="disc" cx="7" cy="7" r="7"/><path class="glyph-fill" d="M4.5 3.6l1.3-.3.8 1.8-.9.7c.4.9 1.1 1.6 2 2l.7-.9 1.8.8-.3 1.3c-2.9.2-5.6-2.5-5.4-5.4z"/></svg></li>
        <li>Nina.Prell@mailbox.example<svg class="contact-icon" viewBox="0 0 14 14"><circle class="disc" cx="7" cy="7" r="7"/><rect class="glyph" x="3.8" y="4.8" width="6.4" height="4.4"/><path class="glyph" d="M3.8 4.8L7 7.4l3.2-2.6"/></svg></li>
        <li>www.marlowbead.example/ninaprell<svg class="contact-icon" viewBox="0 0 14 14"><circle class="disc" cx="7" cy="7" r="7"/><circle class="glyph" cx="7" cy="7" r="3.4"/><path class="glyph" d="M3.6 7h6.8M7 3.6c-1.6 2-1.6 4.8 0 6.8M7 3.6c1.6 2 1.6 4.8 0 6.8"/></svg></li>
      </ul>
      <div class="contact-rule"></div>
      <ul class="contact-list contact-list--social">
        <li>Viewcastlinkcontent<svg class="contact-icon" viewBox="0 0 14 14"><circle class="disc" cx="7" cy="7" r="7"/></svg></li>
        <li>Flitterlinkcontent<svg class="contact-icon" viewBox="0 0 14 14"><circle class="disc" cx="7" cy="7" r="7"/></svg></li>
        <li>workweblinkcontent<svg class="contact-icon" viewBox="0 0 14 14"><circle class="disc" cx="7" cy="7" r="7"/></svg></li>
      </ul>
    </div>
    <p class="option-label">OPTION 03</p>
  </section>

  <section class="option option--04">
    <div class="card card--front">
      <div class="brand-square"></div>
      <p class="holder-name">Rosalind K. Prell</p>
      <p class="holder-title">Esq. Attorney Bar</p>
    </div>
    <div class="card card--back">
      <ul class="contact-list contact-list--direct">
        <li>(555) 482-7716<svg class="contact-icon" viewBox="0 0 14 14"><circle class="disc" cx="7" cy="7" r="7"/><path class="glyph-fill" d="M4.5 3.6l1.3-.3.8 1.8-.9.7c.4.9 1.1 1.6 2 2l.7-.9 1.8.8-.3 1.3c-2.9.2-5.6-2.5-5.4-5.4z"/></svg></li>
        <li>Nina.Prell@mailbox.example<svg class="contact-icon" viewBox="0 0 14 14"><circle class="disc" cx="7" cy="7" r="7"/><rect class="glyph" x="3.8" y="4.8" width="6.4" height="4.4"/><path class="glyph" d="M3.8 4.8L7 7.4l3.2-2.6"/></svg></li>
        <li>www.marlowbead.example/ninaprell<svg class="contact-icon" viewBox="0 0 14 14"><circle class="disc" cx="7" cy="7" r="7"/><circle class="glyph" cx="7" cy="7" r="3.4"/><path class="glyph" d="M3.6 7h6.8M7 3.6c-1.6 2-1.6 4.8 0 6.8M7 3.6c1.6 2 1.6 4.8 0 6.8"/></svg></li>
      </ul>
      <div class="contact-rule"></div>
      <ul class="contact-list contact-list--social">
        <li>Viewcastlinkcontent<svg class="contact-icon" viewBox="0 0 14 14"><circle class="disc" cx="7" cy="7" r="7"/></svg></li>
        <li>Flitterlinkcontent<svg class="contact-icon" viewBox="0 0 14 14"><circle class="disc" cx="7" cy="7" r="7"/></svg></li>
        <li>workweblinkcontent<svg class="contact-icon" viewBox="0 0 14 14"><circle class="disc" cx="7" cy="7" r="7"/></svg></li>
      </ul>
    </div>
    <p class="option-label">OPTION 04</p>
  </section>

</main>
</body>
</html>
```